needs to stand out, but be very clean
Project: Logo for auto broker stationary,
Logo for auto broker stationary,  - Automotive
Logo for auto broker stationary,
Professional
Harbor Motorworks USA
Los Angeles based, Global shipping
Dorian@harbormotorworks-example.com
www.harbormotorworks-example.com
I would like to have at least one file in vector eps, logo and cards. I would like 4 or 6 automotive logos in the corners (4) velorian, Kastra, Tenko, Ardello or (6) Velorian, Kastra, Ardello, Tenko, Ardello, Quellano the other two in the middle of top and bottom. If you like the initials HMU you can use them. working on getting 800 number now, please just put in 555-014-2731 and we can change it later. I was thinking black background for card with white or silver writing and maybe some kind of splash of red.
Pick a font or style you like saying: You don't go to court without an attorney. Why would you buy a car without your Broker?
DorianPlume DorianPlume
I'm surprised that only one person actually read what I wrote and showed me one business card with car logos (kastra, velorian etc. ) on it. I think I like the logo centered.

```html
<!DOCTYPE html>
<html lang="en">
<head>
<meta charset="utf-8">
<title>Harbor Motorworks USA – Business Cards</title>
<link rel="stylesheet" href="https://fonts.googleapis.com/css2?family=Open+Sans:wght@400;600;700&display=swap">
<style>
  :root {
    --bg: #dcdcdc;
    --card-dark: #2b2b2b;
    --card-dark-edge: #1f1f1f;
    --card-light: #ffffff;
    --swoosh-dark: #303030;
    --accent-red: #d3212c;
    --text-light: #f2f2f2;
    --text-dark: #333333;
    --text-muted: #666666;
  }
  * { margin: 0; padding: 0; box-sizing: border-box; }
  html, body { width: 1200px; height: 902px; overflow: hidden; }
  body {
    background: var(--bg);
    font-family: "Open Sans", Arial, sans-serif;
    position: relative;
  }
  .card {
    position: absolute;
    border-radius: 3px;
    overflow: hidden;
    box-shadow: 0 10px 24px rgba(0,0,0,0.22);
  }
  .card--front {
    left: 520px; top: 70px; width: 560px; height: 320px;
    background: linear-gradient(135deg, var(--card-dark) 0%, var(--card-dark-edge) 100%);
    display: flex; align-items: center; justify-content: center;
  }
  .brand {
    text-align: center;
    color: var(--text-light);
    font-weight: 600;
    letter-spacing: 0.08em;
    text-transform: uppercase;
    line-height: 1.25;
  }
  .brand__name { font-size: 30px; }
  .brand__region { font-size: 14px; letter-spacing: 0.5em; display: block; }
  .brand--front .brand__name::before {
    content: ""; display: inline-block; width: 10px; height: 10px;
    background: var(--accent-red); border-radius: 50%;
    margin-right: 12px; vertical-align: middle;
  }

  .card--back {
    left: 290px; top: 470px; width: 640px; height: 366px;
    background: var(--card-light);
  }
  .card__swoosh { position: absolute; inset: 0; width: 100%; height: 100%; }
  .brand--back {
    position: absolute; left: 36px; top: 64px; text-align: left;
    color: var(--text-dark);
  }
  .brand--back .brand__name { font-size: 24px; }
  .brand--back .brand__region { font-size: 12px; padding-left: 100px; }
  .holder { position: absolute; left: 44px; top: 212px; }
  .holder__name { color: var(--accent-red); font-weight: 700; font-size: 17px; }
  .holder__role { color: var(--text-muted); font-size: 14px; margin-top: 2px; }
  .contact {
    position: absolute; right: 30px; top: 72px;
    list-style: none; text-align: right;
    color: var(--text-light); font-size: 11.5px; line-height: 22px;
  }
  .contact li { display: flex; justify-content: flex-end; align-items: center; gap: 8px; }
  .contact svg { width: 11px; height: 11px; fill: var(--text-light); flex: none; }
</style>
</head>
<body>

  <section class="card card--front" aria-label="Business card front">
    <div class="brand brand--front">
      <span class="brand__name">Harbor Motorworks</span>
      <span class="brand__region">USA</span>
    </div>
  </section>

  <section class="card card--back" aria-label="Business card back">
    <svg class="card__swoosh" viewBox="0 0 640 366" preserveAspectRatio="none" aria-hidden="true">
      <path d="M0,338 C170,350 250,250 350,160 C440,80 540,46 640,36 L640,366 L0,366 Z" fill="var(--swoosh-dark)"/>
      <path d="M0,318 C170,332 245,232 345,142 C435,62 540,28 640,18" fill="none" stroke="var(--accent-red)" stroke-width="6"/>
      <path d="M0,350 C180,360 270,262 370,176 C455,104 550,72 640,62" fill="none" stroke="#4a4a4a" stroke-width="2"/>
    </svg>

    <div class="brand brand--back">
      <span class="brand__name">Harbor Motorworks</span>
      <span class="brand__region">USA</span>
    </div>

    <div class="holder">
      <p class="holder__name">Mara Ellis-Crane</p>
      <p class="holder__role">Consultant</p>
    </div>

    <ul class="contact">
      <li>480 Harbor Avenue <svg viewBox="0 0 12 12"><path d="M6 0a4 4 0 0 0-4 4c0 3 4 8 4 8s4-5 4-8a4 4 0 0 0-4-4zm0 5.5a1.5 1.5 0 1 1 0-3 1.5 1.5 0 0 1 0 3z"/></svg></li>
      <li>Los Angeles CA <svg viewBox="0 0 12 12"><path d="M6 0a4 4 0 0 0-4 4c0 3 4 8 4 8s4-5 4-8a4 4 0 0 0-4-4zm0 5.5a1.5 1.5 0 1 1 0-3 1.5 1.5 0 0 1 0 3z"/></svg></li>
      <li>555-014-2731 <svg viewBox="0 0 12 12"><path d="M2.5 0.5l2 2.5-1.2 1.4a7 7 0 0 0 4.3 4.3L9 7.5l2.5 2-1.5 2C5 11.5 0.5 7 0.5 2z"/></svg></li>
      <li>555-014-2731 <svg viewBox="0 0 12 12"><path d="M2.5 0.5l2 2.5-1.2 1.4a7 7 0 0 0 4.3 4.3L9 7.5l2.5 2-1.5 2C5 11.5 0.5 7 0.5 2z"/></svg></li>
      <li>Dorian@harbormotorworks-example.com <svg viewBox="0 0 12 12"><path d="M0 2h12v8H0zm1 1l5 4 5-4z"/></svg></li>
      <li>www.harbormotorworks-example.com <svg viewBox="0 0 12 12"><circle cx="6" cy="6" r="5.5" fill="none" stroke="#f2f2f2" stroke-width="1"/><path d="M0.5 6h11M6 0.5c-3 3-3 8 0 11M6 0.5c3 3 3 8 0 11" fill="none" stroke="#f2f2f2" stroke-width="0.8"/></svg></li>
    </ul>
  </section>

</body>
</html>
```